Lime Wash Direct Mail Postcard Design

I need a postcard that is going to be mailed.
We are a residential and commerical painting company. We are going to start marking our Ventian Plaster, Lime Wash, Roman Clay, Mineral Wash.
I've attached the layout to use that shows bleed and such. I've included a mock up I've done to get an idea of what I want.
- I want it to look sophicated
- Speciality
- Art
I've included logos of 2 companies - Velastra and Cindrel to show.
I want to show mostly interior work but one or 2 lime wash houses that's lighter, shows the bricks in area would be good.
I love the saying "You're unique - Your Home Should Be Too" or if you have a better variation of that, I'd be open to it.

```html
<!DOCTYPE html>
<html lang="en">
<head>
<meta charset="UTF-8">
<title>Brightfield Painting – Direct Mail Postcard</title>
<link href="https://fonts.googleapis.com/css2?family=Russo+One&family=Exo+2:wght@400;600&family=Arimo&display=swap" rel="stylesheet">
<style>
  :root{
    --stage:#a9a9ab;
    --paper:#eeeeee;
    --blue:#5693d0;
    --red:#c8373a;
    --plum:#5a3a47;
    --ink:#1c1c1c;
    --gold:#c9b07a;
    --white:#ffffff;
  }
  *{margin:0;padding:0;box-sizing:border-box}
  html,body{width:1200px;height:1200px;overflow:hidden}
  body{background:var(--stage);position:relative;font-family:"Exo 2",sans-serif;color:var(--ink)}

  .postcard{position:absolute;left:270px;width:660px;height:472px;background:var(--paper);overflow:hidden;box-shadow:0 2px 6px rgba(0,0,0,.25)}
  .postcard--front{top:40px}
  .postcard--back{top:660px}
  .postcard svg.art{position:absolute;inset:0}

  /* front */
  .brand{position:absolute;left:405px;top:62px;display:flex;align-items:center;gap:8px}
  .brand__mark{width:22px;height:22px;background:var(--red)}
  .brand__name{font-family:"Russo One",sans-serif;font-size:19px;color:var(--blue);letter-spacing:.5px}
  .headline{position:absolute;left:405px;top:140px;font-family:"Russo One",sans-serif;font-size:31px;line-height:33px;color:var(--blue)}
  .band{position:absolute;left:405px;width:233px;background:var(--red);color:var(--white);font-family:"Russo One",sans-serif;white-space:nowrap}
  .band--tagline{top:212px;height:35px;font-size:17.5px;line-height:35px;padding-left:7px}
  .band--deadline{top:374px;height:36px;font-size:29px;line-height:37px;padding-left:6px}
  .offer-lead{position:absolute;left:405px;top:253px;font-family:"Russo One",sans-serif;font-size:24px;color:var(--blue);white-space:nowrap}
  .offer-value{position:absolute;left:388px;top:276px;font-family:"Russo One",sans-serif;font-size:101px;line-height:100px;color:var(--blue);letter-spacing:-3px}
  .offer-off{position:absolute;left:596px;top:290px;font-family:"Russo One",sans-serif;font-size:19px;color:var(--red)}
  .partners{position:absolute;left:405px;top:426px;display:flex;gap:26px;font-family:"Exo 2",sans-serif;font-weight:600;font-size:19px}
  .partner--dark{color:var(--ink)}
  .partner--gold{color:var(--gold)}

  /* back */
  .postage{position:absolute;left:523px;width:121px;border:1.3px solid var(--ink);background:var(--paper);font-family:"Arimo",sans-serif;font-size:8.3px;line-height:10.3px;color:var(--ink)}
  .postage--indicia{top:17px;height:51px;text-align:center;padding-top:4px}
  .postage--indicia .big{font-size:11px;line-height:13px}
  .postage--address{top:73px;height:39px;padding:8px 0 0 8px}
  .section-title{position:absolute;left:22px;font-family:"Russo One",sans-serif;font-size:17.5px;line-height:21px;color:var(--red)}
  .section-title--res{top:210px}
  .section-title--com{top:332px}
  .copy{position:absolute;left:22px;font-size:12.2px;line-height:15.7px;color:var(--ink)}
  .copy--res{top:262px;width:262px}
  .copy--com{top:360px;width:630px}
  .copy--com p+p{margin-top:7px}
</style>
</head>
<body>

<section class="postcard postcard--front" aria-label="Postcard front">
  <svg class="art" width="660" height="472" viewBox="0 0 660 472">
    <defs>
      <clipPath id="kitchen-clip"><circle cx="172" cy="220" r="220"/></clipPath>
    </defs>
    <path d="M0,0 H290 C350,50 392,150 382,262 C372,340 320,400 240,472 H50 C20,472 0,460 0,440 Z" fill="var(--blue)"/>
    <path d="M190,472 C270,425 335,370 354,300 C372,350 392,410 400,472 Z" fill="var(--red)"/>
    <path d="M120,472 C215,440 305,390 354,300 L356,318 C320,390 260,435 190,472 Z" fill="var(--plum)"/>
    <circle cx="172" cy="220" r="226" fill="var(--white)"/>
    <rect role="img" aria-label="Photo of a bright modern kitchen with wood cabinets, white tile and appliances" x="-60" y="-10" width="460" height="460" fill="url(#kitchen-tone)" clip-path="url(#kitchen-clip)"/>
    <defs>
      <linearGradient id="kitchen-tone" x1="0" y1="0" x2="0" y2="1">
        <stop offset="0" stop-color="#d9d7d4"/>
        <stop offset=".45" stop-color="#c2a27c"/>
        <stop offset="1" stop-color="#b48d62"/>
      </linearGradient>
    </defs>
  </svg>

  <div class="brand"><span class="brand__mark"></span><span class="brand__name">BRIGHTFIELD PAINTING</span></div>
  <h1 class="headline">YOU’RE<br>UNIQUE</h1>
  <div class="band band--tagline">Your home should be too</div>
  <div class="offer-lead">Free consultation</div>
  <div class="offer-value">10%</div>
  <div class="offer-off">OFF</div>
  <div class="band band--deadline">thru Jan 31st</div>
  <div class="partners">
    <span class="partner--dark">VELASTRA</span>
    <span class="partner--gold">CINDREL</span>
  </div>
</section>

<section class="postcard postcard--back" aria-label="Postcard back">
  <svg class="art" width="660" height="472" viewBox="0 0 660 472">
    <defs>
      <linearGradient id="bedroom-tone" x1="0" y1="0" x2="0" y2="1">
        <stop offset="0" stop-color="#e4e2de"/>
        <stop offset=".6" stop-color="#d8d2c6"/>
        <stop offset="1" stop-color="#c9d6d4"/>
      </linearGradient>
      <linearGradient id="storefront-tone" x1="0" y1="0" x2="0" y2="1">
        <stop offset="0" stop-color="#a9c3de"/>
        <stop offset=".45" stop-color="#b7b9bc"/>
        <stop offset="1" stop-color="#5e5f62"/>
      </linearGradient>
    </defs>
    <circle cx="723" cy="260" r="121" fill="var(--blue)"/>
    <circle cx="277" cy="115" r="118" fill="var(--blue)"/>
    <circle cx="277" cy="115" r="109" fill="var(--white)"/>
    <circle role="img" aria-label="Photo of a calm bedroom with panelled wall, tufted headboard and pendant lantern" cx="277" cy="115" r="106" fill="url(#bedroom-tone)"/>
    <circle cx="432" cy="201" r="118" fill="var(--red)"/>
    <circle cx="432" cy="201" r="109" fill="var(--white)"/>
    <circle role="img" aria-label="Photo of a commercial storefront being repainted by a crew" cx="432" cy="201" r="106" fill="url(#storefront-tone)"/>
  </svg>

  <div class="postage postage--indicia">PRESORTED STANDARD<br>U.S. POSTAGE PAID<br>ROUTE PERMIT<br><span class="big">ECRWSS</span></div>
  <div class="postage postage--address">LOCAL<br>POSTAL CUSTOMER</div>

  <h2 class="section-title section-title--res">Grand Rapids<br>Residential Painter</h2>
  <p class="copy copy--res">From start to finish, we will guide you the entire way with transparent expectations, excellent customer service and a top-of the-line, quality paint team.</p>

  <h2 class="section-title section-title--com">Grand Rapids Commercial Painting Service</h2>
  <div class="copy copy--com">
    <p>Are you looking for a Grand Rapids painting company that understands the importance of making your property look its best — with the least disruption to your customers or tenants?</p>
    <p>Well, look no further than the professional and experienced Grand Rapids painters at Brightfield Painting. We have successfully built our commercial painting reputation over many years of expertly painting properties just like yours.</p>
  </div>
</section>

</body>
</html>
```